Business Card Design Project

looking for a stylish and simple double sided business card.
I am an artist - specialising in fashion illustration, portraits and murals.
the front should be simply my name and tag:

D A V E R U
Painted with life

My preference is for a Black background with DAVERU in red or embossed.
Painted with life in White or multi-coloured.

the back will have detail:

Personalised Art
Portraits, Murals, Fashion Illustration

0487 312 560
daveru@daveru.com.au
www.daveru.com.au

Target Market(s)

Adults that are based in western speaking countries who have an appreciation for art and design. Portraits and wall art
Business owners who may need personalised all art for their business space. Murals and personalised canvass.
People in the fashion industry, who may require fashion illustrations.

Industry/Entity Type

Fashion

Requirements
Must have
• BOLD but simple at the same time, timeless modern element to it.
Nice to have
• simple lettering
Should not have
• Not too busy or wordy,

```html
<!DOCTYPE html>
<html lang="en">
<head>
<meta charset="utf-8">
<title>Daveru – Business Card</title>
<link rel="stylesheet" href="https://fonts.googleapis.com/css2?family=Cinzel:wght@400;700&family=Crimson+Text:wght@400&family=Kaushan+Script&display=swap">
<style>
  :root {
    --stage: #1b1c1d;
    --card-red: #b8141c;
    --card-red-deep: #8e0d13;
    --card-black: #151515;
    --ink-white: #f4f2f0;
    --ink-grey: #d6d6d6;
    --ink-black: #141010;
    --accent-red: #c4161d;
  }
  * { box-sizing: border-box; margin: 0; padding: 0; }
  html, body {
    width: 1200px; height: 900px; overflow: hidden;
    background: var(--stage);
  }
  .canvas {
    position: relative; width: 1200px; height: 900px;
    display: flex; flex-direction: column; align-items: center; justify-content: center; gap: 40px;
  }
  .card {
    position: relative; width: 600px; height: 343px;
    border-radius: 3px; overflow: hidden;
    box-shadow: 0 14px 30px rgba(0,0,0,.55);
  }

  /* Front */
  .card--front {
    background: radial-gradient(ellipse at 70% 35%, var(--card-red) 0%, var(--card-red-deep) 100%);
  }
  .brand {
    position: absolute; right: 50px; top: 120px; text-align: right;
  }
  .brand__mark {
    display: block; width: 30px; height: 30px; border-radius: 50%;
    background: var(--ink-white); margin: 0 0 18px auto;
  }
  .brand__name {
    font-family: "Cinzel", serif; font-weight: 400;
    font-size: 54px; line-height: 1; letter-spacing: 2px;
    color: var(--ink-white);
  }
  .brand__tag {
    margin-top: 6px;
    font-family: "Cinzel", serif; font-weight: 400;
    font-size: 19px; letter-spacing: 5px;
    color: var(--ink-black);
  }

  /* Back */
  .card--back { background: var(--card-black); }
  .contact {
    position: absolute; left: 44px; top: 36px;
    font-family: "Crimson Text", serif; font-size: 18px; line-height: 1.22;
    color: var(--ink-grey); list-style: none;
  }
  .offer {
    position: absolute; left: 0; right: 0; top: 230px; text-align: center;
  }
  .offer__title {
    font-family: "Kaushan Script", cursive; font-size: 27px; letter-spacing: 1px;
    color: var(--accent-red); line-height: 1;
  }
  .services {
    margin-top: 4px;
    font-family: "Cinzel", serif; font-weight: 700; font-size: 17px; letter-spacing: .5px;
    color: var(--ink-grey); white-space: nowrap;
  }
  .services__initial { color: var(--accent-red); }
  .services__dot { margin: 0 6px; color: var(--ink-grey); }
  .band {
    position: absolute; left: 0; right: 0; bottom: 0; height: 58px;
    background: linear-gradient(180deg, var(--card-red) 0%, var(--card-red-deep) 100%);
  }
</style>
</head>
<body>
<main class="canvas">
  <section class="card card--front" aria-label="Card front">
    <div class="brand">
      <span class="brand__mark" aria-hidden="true"></span>
      <h1 class="brand__name">DAVERU</h1>
      <p class="brand__tag">PAINTED WITH LIFE</p>
    </div>
  </section>

  <section class="card card--back" aria-label="Card back">
    <ul class="contact">
      <li>web: www.daveru.com.au</li>
      <li>phone: 0487 312 560</li>
      <li>mail: daveru@daveru.com.au</li>
    </ul>
    <div class="band"></div>
    <div class="offer">
      <h2 class="offer__title">PERSONALISED ART</h2>
      <p class="services">
        <span class="services__dot">•</span><span class="services__initial">P</span>ORTRAITS
        <span class="services__dot">•</span><span class="services__initial">M</span>URALS
        <span class="services__dot">•</span><span class="services__initial">F</span>ASHION ILLUSTRATION
      </p>
    </div>
  </section>
</main>
</body>
</html>
```